依頼詳細
留学生向けのアルバイト募集のA4チラシ(印刷後壁に貼り付け)を作成します。複数の企業が参加し、共通のテンプレートを使用し、1店舗(例:xx居酒屋 xx店)1枚で印刷します。そこでその雛形のデザインをお願いしたいと思います。
レイアウトは添付ファイルにこだわる必要はないです。
*どのような業種職種でも使える汎用性の高いデザインでお願いします。
記載項目
ロゴ(写真データ)/紹介写真(写真データ)店名/業種/給与/勤務時間/最寄駅/PR文/応募条件/応募連絡先/先輩の声/先輩の写真(写真データ)/名前/出身/年齢/日本語レベル/在日期間
また、テキスト入力の部分は名前/出身/年齢/日本語レベル/在日期間を除く全ての部分にふりがなを付けられるようにしてください。(添付ファイル参照)

写真データ以外は全てテキストデータで入力

```html
<!DOCTYPE html>
<html lang="ja">
<head>
<meta charset="utf-8">
<title>アルバイト募集</title>
<link href="https://fonts.googleapis.com/css2?family=Noto+Sans+JP:wght@400;700&family=Noto+Serif+JP:wght@400;700&display=swap" rel="stylesheet">
<style>
:root{
  --green:#8cc63e;
  --green-dark:#6fa82a;
  --red:#e0201c;
  --ink:#222;
  --sub:#666;
  --line:#bbb;
  --photo:#cfcfcf;
  --card:#d9d9d9;
}
*{margin:0;padding:0;box-sizing:border-box}
html,body{width:893px;height:1200px;overflow:hidden;background:#fff}
body{font-family:"Noto Sans JP",sans-serif;color:var(--ink);position:relative}
.serif{font-family:"Noto Serif JP",serif}
.header{position:absolute;left:0;top:0;width:893px;height:100px;background:var(--green);color:#fff}
.logo{position:absolute;left:18px;top:12px;width:76px;height:76px;border-radius:50%;background:#fff;color:var(--sub);display:flex;align-items:center;justify-content:center;font-size:16px}
.store-label{position:absolute;left:118px;top:14px;font-size:22px}
.store-en{position:absolute;left:118px;top:62px;font-size:13px}
.store-kana{position:absolute;left:230px;top:10px;font-size:12px;letter-spacing:2px}
.store-name{position:absolute;left:230px;top:28px;font-size:50px;font-weight:700;font-family:"Noto Serif JP",serif;letter-spacing:2px;line-height:1.3}
.contact{position:absolute;left:22px;top:108px;width:850px}
.company{font-size:20px;font-weight:700;line-height:1.4}
.tel{position:absolute;right:0;top:-4px;font-size:32px;font-weight:700;color:var(--red);line-height:1.3}
.kana{font-size:9px;color:var(--sub);letter-spacing:1px;line-height:1.3}
.address{font-size:13px;font-weight:700;line-height:1.4}
.info{position:absolute;left:22px;top:178px;width:520px;border-top:1px solid var(--line)}
.row{display:flex;height:66px;border-bottom:1px solid var(--line)}
.row .label{width:132px;padding:6px 0 0 8px;font-size:15px;font-weight:700}
.row .label em{display:block;font-style:normal;font-weight:400;color:var(--green);font-size:12px;margin-top:6px}
.row .value{flex:1;padding-top:4px}
.big{font-size:22px;font-family:"Noto Serif JP",serif;font-weight:700;line-height:1.4}
.photo{position:absolute;left:562px;top:178px;width:310px;height:262px;background:var(--photo);display:flex;align-items:center;justify-content:center;color:#888;font-size:14px}
.quals{position:absolute;left:22px;top:454px;width:850px;height:70px;border:2px solid var(--red);display:flex}
.quals .label{width:132px;padding:8px 0 0 8px;font-size:15px;font-weight:700}
.quals .label em{display:block;font-style:normal;font-weight:400;color:var(--green);font-size:12px;margin-top:6px}
.quals .value{padding-top:6px;flex:1}
.qual-line{display:flex}
.qual-line span{width:240px}
.pr-head{position:absolute;left:22px;top:538px;font-size:22px;color:var(--green);font-weight:700;line-height:1.2}
.pr-head span{font-size:16px}
.pr-rule{position:absolute;left:170px;top:556px;width:702px;height:2px;background:var(--green)}
.pr-text{position:absolute;left:22px;top:568px;width:850px;font-size:16px;line-height:1.3}
.pr-text p{margin-bottom:2px}
.cards{position:absolute;left:22px;top:646px;width:850px;display:flex;gap:28px}
.card{flex:1;border:2px solid var(--card)}
.card-top{background:var(--card);height:190px;position:relative;padding:10px 12px}
.card-title{background:var(--green);color:#fff;font-size:12px;display:inline-block;padding:1px 10px;border-radius:3px;margin-bottom:6px}
.card table{border-collapse:collapse;font-size:12px;background:#fff;table-layout:fixed;width:196px}
.card td{border:1px solid var(--line);padding:2px 6px;height:26px;white-space:nowrap}
.card td:first-child{width:96px}
.card .photo-sm{position:absolute;right:12px;top:14px;width:170px;height:162px;background:#bdbdbd;display:flex;align-items:center;justify-content:center;color:#888;font-size:13px}
.card-text{padding:12px 12px;font-size:13px;line-height:1.75;height:330px}
.bottom{position:absolute;left:0;top:1186px;width:893px;height:14px;background:var(--green)}
</style>
</head>
<body>
<header class="header">
  <div class="logo">logo</div>
  <div class="store-label">店名</div>
  <div class="store-en">Store name</div>
  <div class="store-kana">マルマルイザカヤ　バツバツテン</div>
  <div class="store-name">○○居酒屋 ××店</div>
</header>

<section class="contact">
  <div class="company serif">株式会社 XXX　アルバイト採用係</div>
  <div class="tel">tel 03-0000-0000</div>
  <div class="kana">トウキョウトチュウオウクシンカワ ニチョウメ ハチバン ジュウヨンゴウ ダイサンミドリビル ゴカイ</div>
  <div class="address serif">東京都中央区新川２丁目８番１４号　第三みどりビル５階</div>
</section>

<section class="info">
  <div class="row"><div class="label">業種<em>Business</em></div><div class="value"><div class="kana">インショクセッキャク／キッチン</div><div class="big">①飲食接客／②キッチン</div></div></div>
  <div class="row"><div class="label">給与<em>Payroll</em></div><div class="value"><div class="kana">キュウヨ</div><div class="big">① ¥1,000/h／② ¥980/h</div></div></div>
  <div class="row"><div class="label">勤務時間<em>Working hours</em></div><div class="value"><div class="kana">ヘイジツドニチ 6:30～24:00</div><div class="big">平日土日　6:30～24:00</div></div></div>
  <div class="row"><div class="label">最寄り駅<em>Nearest station</em></div><div class="value"><div class="kana">アカサカ／アカサカミツケ／タメイケサンノウ</div><div class="big">赤坂／赤坂見附／溜池山王</div></div></div>
</section>
<div class="photo" role="img" aria-label="店舗紹介写真">Photo</div>

<section class="quals">
  <div class="label">応募条件<em>Qualifications</em></div>
  <div class="value">
    <div class="kana qual-line"><span>①N4イジョウ（ソウダンオウ）</span><span>②N3イジョウ（ソウダンオウ）</span></div>
    <div class="big qual-line"><span>① N4以上（応相談）</span><span>② N3以上（応相談）</span></div>
  </div>
</section>

<div class="pr-head">P<span>ublic</span> R<span>elations</span></div>
<div class="pr-rule"></div>
<section class="pr-text serif">
  <div class="kana">リュウガクセイダイカンゲイ ニホンゴガアマリシャベルコトガデキナクテモ ニホンゴレベル</div>
  <p>留学生大歓迎！日本語があまり喋ることができなくても、日本語レベル</p>
  <div class="kana">ニアワセシドウイタシマス シフトハソウダンカノウデス</div>
  <p>に合わせ指導致します。学校行事にも対応！朝6:30～深夜までシフト相談可！</p>
</section>

<section class="cards">
  <article class="card">
    <div class="card-top">
      <div class="card-title">先輩の声</div>
      <table>
        <tr><td>名前</td><td>グエン・ミン</td></tr>
        <tr><td>出身</td><td>ベトナム</td></tr>
        <tr><td>年齢</td><td>22才</td></tr>
        <tr><td>日本語レベル</td><td>N3</td></tr>
        <tr><td>在日期間</td><td>2年</td></tr>
      </table>
      <div class="photo-sm" role="img" aria-label="先輩スタッフの写真">Photo</div>
    </div>
    <div class="card-text serif">初めてのアルバイトでしたが、先輩が丁寧に仕事を教えてくれるので安心して働けています。日本語を使う機会が多く、会話も上達しました。学校のテストの時期にはシフトを調整してもらえるので、勉強と両立できます。みなさんも一緒に働きましょう！</div>
  </article>
  <article class="card">
    <div class="card-top">
      <div class="card-title">先輩の声</div>
      <table>
        <tr><td>名前</td><td>リ・ファン</td></tr>
        <tr><td>出身</td><td>中国</td></tr>
        <tr><td>年齢</td><td>24才</td></tr>
        <tr><td>日本語レベル</td><td>N2</td></tr>
        <tr><td>在日期間</td><td>3年</td></tr>
      </table>
      <div class="photo-sm" role="img" aria-label="先輩スタッフの写真">Photo</div>
    </div>
    <div class="card-text serif">お店のみなさんはとても優しく、困ったときはすぐに助けてくれます。お客様との会話を通して、教科書では学べない日本語や文化を知ることができました。まかないもおいしいです。ここで働いて本当によかったと思っています。</div>
  </article>
</section>

<div class="bottom"></div>
</body>
</html>
```